Summit Crest Advisory - White Collar Engineering Consultancy

I'm chasing a website to provide high level information about what Summit Crest Advisory is and service's we provide - only chasing something simple. We are a new white collar secondment/contractor/professional services/consultancy specialising is providing the best consultants into contractor roles.

Our primary industries are energy, gas, pipelines, water processing, power, projects, geographic information systems, design, accounting.

Our people are mechanical,/electrical/civil/process/chemical engineers, project engineers, project managers, technical experts, GIS analysts, integrity engineers, pipeline engineers,

Currently I have this domain registered through nimbledns - https://www.scadvisoryhub.com/

I'd like to keep this domain but completely overhaul the website to be sleek and follow the logo styling.

Example websites within my industry that I like:
- https://www.bramwellfieldworks.com.au/
- https://quorvin.com.au/
- https://www.hlmtec.com.au/

I'd like the winner to code and assist with making the website functional under my domain.

Would like to include:
- industries
- services
- why work with us
- terms and conditions as per attached
- location (Brisbane)
- contact us form, that submits an email to jordan.pryce@scadvisoryhub.com
- WorkCircle link

Would definitely be looking to polish the winning result with the designer over the phone or via email.

I will also add some infrastructure photos for use; otherwise please use generic CSG related infrastructure.

Cheers,

Jordan

Industry/Entity Type

Energy, resources, gas, mining, geographic information systems, accounting, construction.

Coding

Coded - Design and coding required

Number of Pages Required

4 page

Colors
0054AA
0677BA
7BADD7
CADEEF
E8F1F8

Requirements
Must have
• Refer to project description

```html
<!DOCTYPE html>
<html lang="en">
<head>
<meta charset="utf-8">
<title>Summit Crest Advisory – White Collar Engineering Consultancy</title>
<link rel="stylesheet" href="https://fonts.googleapis.com/css2?family=Montserrat:wght@400;500;600;700&family=Oswald:wght@600&display=swap">
<style>
:root{
  --blue-deep:#0054AA;
  --blue:#0677BA;
  --blue-mid:#7BADD7;
  --blue-pale:#CADEEF;
  --blue-mist:#E8F1F8;
  --ink:#1c1c1c;
  --charcoal:#333536;
  --night:#0e0f10;
  --grey-bg:#f1f1f1;
  --line:#d9dde2;
  --white:#ffffff;
}
*{box-sizing:border-box;margin:0;padding:0}
html,body{width:1200px;height:3841px;overflow:hidden}
body{position:relative;font-family:"Montserrat",sans-serif;color:var(--ink);background:var(--white)}
.abs{position:absolute}
.btn{position:absolute;display:flex;align-items:center;justify-content:center;background:var(--blue-deep);color:var(--white);font-size:12px;font-weight:600;border-radius:2px}
.brand{display:flex;align-items:center;gap:8px;color:var(--white);font-weight:600;font-size:19px}
.brand .dot{width:28px;height:28px;border-radius:50%;background:var(--white)}

/* nav */
.site-nav{left:0;top:0;width:1200px;height:64px;background:var(--night);z-index:3}
.site-nav .brand{position:absolute;left:161px;top:18px}
.site-nav a{position:absolute;top:24px;color:#d8d8d8;font-size:12px;text-decoration:none}
.site-nav a.active{color:var(--white);font-weight:600}

/* hero */
.hero{left:0;top:64px;width:1200px;height:513px;overflow:hidden;
  background:
    radial-gradient(ellipse 420px 300px at 860px 160px,rgba(120,110,95,.55),transparent 70%),
    radial-gradient(ellipse 300px 260px at 1080px 120px,rgba(170,120,70,.35),transparent 70%),
    radial-gradient(ellipse 500px 260px at 900px 460px,rgba(60,70,80,.5),transparent 70%),
    linear-gradient(90deg,#141516 0%,#1b1c1e 38%,#2b2e31 60%,#3b3d3f 100%)}
.hero-shade{position:absolute;inset:0;background:linear-gradient(90deg,rgba(8,9,10,.92) 0%,rgba(8,9,10,.6) 42%,rgba(8,9,10,.15) 100%)}
.hero h1{position:absolute;left:162px;top:150px;color:var(--white);font-weight:500;font-size:37px;line-height:1.2;letter-spacing:.3px}
.hero .lead{position:absolute;left:162px;top:198px;color:var(--white);font-family:"Oswald",sans-serif;font-weight:600;font-size:45px;line-height:53px}

/* about */
.about-photo{left:161px;top:663px;width:374px;height:525px;
  background:
    radial-gradient(ellipse 120px 70px at 210px 80px,rgba(240,190,40,.75),transparent 70%),
    radial-gradient(ellipse 90px 60px at 300px 130px,rgba(240,190,40,.6),transparent 70%),
    radial-gradient(ellipse 150px 200px at 200px 300px,rgba(170,195,225,.8),transparent 70%),
    radial-gradient(ellipse 120px 180px at 310px 330px,rgba(50,60,80,.7),transparent 70%),
    linear-gradient(160deg,#9aa09f 0%,#b9bcb6 30%,#7f878a 65%,#4a525a 100%)}
.eyebrow{left:610px;top:690px;color:var(--blue-deep);font-size:13px;font-weight:600;display:flex;align-items:center;gap:8px}
.eyebrow::after{content:"";width:16px;height:2px;background:var(--blue-deep)}
.about h2{position:absolute;left:610px;top:718px;font-size:32px;font-weight:600}
.about-copy{position:absolute;left:610px;width:430px;font-size:12.4px;line-height:23px;color:#2a2a2a}
.stat{position:absolute;top:1105px;height:126px;color:var(--white);padding:22px 38px}
.stat strong{display:block;font-size:31px;font-weight:500;margin-bottom:6px}
.stat span{font-size:13px;line-height:20px;display:block}

/* services */
.services{left:0;top:1322px;width:1200px;height:671px;background:var(--grey-bg)}
.section-title{position:absolute;left:0;width:1200px;text-align:center;color:var(--blue-deep);font-size:32px;font-weight:700}
.service-card{position:absolute;top:143px;width:277px;height:375px;display:flex;flex-direction:column;justify-content:flex-end;align-items:center;padding-bottom:22px;color:var(--white);font-size:15px;font-weight:600}
.service-card .label{position:relative}
.service-card::after{content:"";position:absolute;left:0;right:0;bottom:0;height:110px;background:linear-gradient(180deg,transparent,rgba(0,0,0,.55))}
.service-card .label{z-index:1}
.service-card.dim{justify-content:center;padding:0 30px;text-align:center}
.service-card.dim::after{display:none}
.service-card.dim p{font-size:12.5px;font-weight:400;line-height:23px;margin-top:8px;color:#e4e4e4}
.arrow{position:absolute;width:38px;height:38px;border-radius:50%;display:flex;align-items:center;justify-content:center}

/* why */
.why{left:0;top:1993px;width:1200px;height:596px;
  background:
    radial-gradient(ellipse 500px 300px at 200px 120px,rgba(120,170,220,.25),transparent 70%),
    radial-gradient(ellipse 400px 200px at 1000px 520px,rgba(10,60,130,.4),transparent 70%),
    linear-gradient(100deg,#0b5fb0 0%,#1b70bc 45%,#1266b4 100%)}
.why h2{position:absolute;left:163px;top:220px;color:var(--white);font-size:31px;font-weight:700}
.why-copy{position:absolute;left:163px;top:267px;width:380px;color:#e9f1f9;font-size:17.5px;line-height:27px}
.why-card{position:absolute;width:199px;height:198px;background:var(--white);border-radius:3px;display:flex;flex-direction:column;align-items:center;justify-content:center;gap:16px;text-align:center;color:var(--blue);font-size:15px;font-weight:600;line-height:19px}

/* terms */
.terms-frame{left:0;top:2589px;width:599px;height:375px;background:#2b2b2b}
.terms-doc{position:absolute;left:10px;top:12px;width:576px;height:363px;background:var(--white);overflow:hidden;font-size:7.6px;line-height:9.4px;color:#222}
.terms-doc .col{position:absolute;width:240px}
.terms-doc b{font-weight:700}
.terms-doc .cl{margin-bottom:4px}
.doc-bar{position:absolute;left:193px;top:318px;width:194px;height:29px;border-radius:15px;background:#3a3a3a;color:#eee;font-size:9px;display:flex;align-items:center;gap:10px;padding:0 12px}
.doc-bar .pg{background:#222;padding:2px 6px;border-radius:2px}
.terms-title{position:absolute;left:680px;top:2710px;color:var(--blue-deep);font-size:32px;font-weight:600}
.terms-copy{position:absolute;left:680px;top:2766px;width:360px;font-size:13px;line-height:27px;color:#2a2a2a}

/* contact */
.contact-intro{left:300px;top:3098px;width:600px;text-align:center;font-size:12.4px;line-height:25px;color:#2a2a2a}
.field{position:absolute;left:161px;width:416px;border:1px solid var(--line);border-radius:3px;display:flex;align-items:flex-start;padding-top:17px;padding-left:48px;font-size:12.5px;color:#333}
.field svg{position:absolute;left:14px;top:15px}
.field i{color:#d42020;font-style:normal}
.submit{position:absolute;left:161px;top:3494px;width:120px;height:36px;border-radius:18px;background:var(--blue-deep);color:var(--white);font-size:12px;font-weight:700;display:flex;align-items:center;gap:12px;padding-left:4px}
.submit .ring{width:28px;height:28px;border-radius:50%;background:var(--white);display:flex;align-items:center;justify-content:center}
.map-frame{left:626px;top:3175px;width:413px;height:358px;background:var(--white);box-shadow:0 4px 18px rgba(0,0,0,.12);padding:9px}
.map-fill{width:100%;height:100%;
  background:
    radial-gradient(ellipse 80px 60px at 60px 150px,rgba(180,215,175,.8),transparent 70%),
    radial-gradient(ellipse 90px 50px at 310px 110px,rgba(200,225,240,.8),transparent 70%),
    radial-gradient(ellipse 70px 50px at 90px 300px,rgba(190,220,185,.7),transparent 70%),
    linear-gradient(135deg,#eef0ec 0%,#e6ebe4 45%,#e3e9ef 100%)}

/* footer */
.site-footer{left:0;top:3597px;width:1200px;height:244px;background:var(--blue-deep);color:var(--white)}
.site-footer .brand{position:absolute;left:161px;top:32px;font-size:17px}
.site-footer .brand .dot{width:24px;height:24px}
.site-footer nav a{position:absolute;top:46px;color:var(--white);font-size:12px;text-decoration:none}
.rule{position:absolute;left:161px;width:878px;height:1px;background:rgba(255,255,255,.3)}
.info{position:absolute;top:107px;display:flex;gap:16px;font-size:12px;line-height:21px}
.info .ic{width:34px;height:34px;border-radius:50%;border:1px solid rgba(255,255,255,.7);display:flex;align-items:center;justify-content:center;flex:none}
.info strong{font-weight:600}
.copy{position:absolute;left:161px;top:203px;font-size:11.5px}
.social{position:absolute;right:161px;top:197px;display:flex;align-items:center;gap:8px;font-size:11px}
.social .dot{width:26px;height:26px;border-radius:50%;border:1.5px solid var(--white)}
</style>
</head>
<body>

<header class="abs site-nav">
  <div class="brand"><span class="dot"></span>Summit Crest Advisory</div>
  <a class="active" style="left:504px">Home</a>
  <a style="left:592px">About Us</a>
  <a style="left:702px">Services</a>
  <a style="left:802px">Industries</a>
  <span class="btn" style="left:911px;top:15px;width:128px;height:36px">Contact Us</span>
</header>

<section class="abs hero" role="img" aria-label="Two engineers in hard hats reviewing a tablet in an industrial plant">
  <div class="hero-shade"></div>
  <h1>We Are A Professionals</h1>
  <p class="lead">White Collar Engineering<br>Consultancy Business.</p>
  <span class="btn" style="left:161px;top:318px;width:127px;height:37px">Contact Us</span>
</section>

<section class="about">
  <div class="abs about-photo" role="img" aria-label="Engineer and colleague in yellow hard hats reviewing a clipboard in a factory"></div>
  <div class="abs eyebrow">About Us</div>
  <h2>About Summit Crest Advisory</h2>
  <p class="about-copy" style="top:768px">Lorem ipsum dolor sit amet, consectetur adipiscing elit. Integerlestie mauris eget iaculis commodo. Pellentesque rhoncus sed ante sedet. Donec lorem justo, tincidunt bibendum urna eu, aliquam scelerisque tellus. Duis consectetur lacus et odio gravida ornare.</p>
  <p class="about-copy" style="top:872px">aptent taciti sociosqu ad litora torquent per conubia nostraincepto s himenaeos. Quisque dapibus arcu ut arcu congue tempor. Etiam a lacus nec ipsum efficitur pulvinar.</p>
  <p class="about-copy" style="top:953px">Nunc pellentesque mi quis eratnd auctor. Nunc vestibulum tincidunt urna, ac dictum orci convallis eu. In vitae ipsum at urna cursus sollicitudin. Sed placerat ipsum mi, sitet blandit sapien hendrerit at.</p>
  <span class="btn" style="left:610px;top:1037px;width:126px;height:36px">Contact Us</span>
  <div class="stat" style="left:428px;width:203px;background:var(--blue)"><strong>38</strong><span>Lorem ipsum dolor<br>sit amet</span></div>
  <div class="stat" style="left:632px;width:202px;background:var(--charcoal)"><strong>2002</strong><span>Lorem ipsum dolor<br>sit amet</span></div>
  <div class="stat" style="left:836px;width:203px;background:var(--blue)"><strong>$5B+</strong><span>Lorem ipsum dolor<br>sit amet</span></div>
</section>

<section class="abs services">
  <h2 class="section-title" style="top:82px">Our Services</h2>
  <span class="arrow" style="left:101px;top:311px;border:1.5px solid #222">
    <svg width="12" height="12" viewBox="0 0 12 12"><path d="M8 1 3 6l5 5" fill="none" stroke="#222" stroke-width="2"/></svg>
  </span>
  <div class="service-card" style="left:161px;background:radial-gradient(ellipse 60px 40px at 100px 150px,rgba(240,190,40,.7),transparent 70%),radial-gradient(ellipse 70px 50px at 200px 110px,rgba(235,235,235,.6),transparent 70%),linear-gradient(180deg,#7f93a8 0%,#a3adb6 35%,#6a737b 70%,#4c545b 100%)" role="img" aria-label="Engineers in hard hats discussing plans on a factory floor"><span class="label">Engineering</span></div>
  <div class="service-card dim" style="left:461px;background:radial-gradient(ellipse 120px 160px at 180px 130px,rgba(110,105,80,.5),transparent 70%),linear-gradient(160deg,#454641,#2c2d2b 60%,#1f2021)" role="img" aria-label="Construction site team in safety vests">
    <svg width="44" height="44" viewBox="0 0 44 44" fill="none" stroke="#fff" stroke-width="2"><path d="M6 32h32M9 32c0-9 6-16 13-16s13 7 13 16"/><path d="M18 16v-5h8v5M22 11v10"/><rect x="8" y="32" width="28" height="4" rx="1"/></svg>
    <div style="margin-top:14px">Construction Management</div>
    <p>Nunc pellentesque mi quis eratnd auctor. Nunc vestibulum tincidunt urna ac dictum orci.</p>
  </div>
  <div class="service-card" style="left:762px;background:radial-gradient(ellipse 60px 90px at 200px 220px,rgba(170,40,30,.55),transparent 70%),radial-gradient(ellipse 80px 60px at 110px 250px,rgba(235,235,230,.7),transparent 70%),linear-gradient(180deg,#9ea3a8 0%,#80868b 40%,#5a544f 100%)" role="img" aria-label="Two inspectors in face masks reviewing documents"><span class="label">Audit &amp; Inspection</span></div>
  <span class="arrow" style="left:1060px;top:317px;background:var(--blue-deep)">
    <svg width="12" height="12" viewBox="0 0 12 12"><path d="M4 1l5 5-5 5" fill="none" stroke="#fff" stroke-width="2"/></svg>
  </span>
  <span class="btn" style="left:537px;top:549px;width:126px;height:36px">Contact Us</span>
</section>

<section class="abs why" role="region" aria-label="Why work with us">
  <h2>Why Work With Us</h2>
  <p class="why-copy">Lorem ipsum dolor sit amet, consectetur adipiscing elit. In in orci sem. In mattis fermentum pharetra. Sed maximus risus dignissim purus pharetra ac.</p>
  <div class="why-card" style="left:628px;top:110px">
    <svg width="62" height="44" viewBox="0 0 62 44" fill="none" stroke="currentColor" stroke-width="2"><circle cx="31" cy="10" r="7"/><circle cx="13" cy="14" r="6"/><circle cx="49" cy="14" r="6"/><path d="M18 42V30c0-6 6-10 13-10s13 4 13 10v12M3 40v-9c0-4 4-7 10-7M59 40v-9c0-4-4-7-10-7"/></svg>
    <div>Lorem Ipsum<br>Dolor</div>
  </div>
  <div class="why-card" style="left:839px;top:72px">
    <svg width="60" height="60" viewBox="0 0 60 60" fill="none" stroke="currentColor" stroke-width="2"><rect x="8" y="8" width="32" height="44" rx="2"/><path d="M18 8V4h12v4M14 20h16M14 28h10M14 36h8"/><circle cx="38" cy="38" r="10"/><path d="M33 38l4 4 6-7M45 45l9 9"/></svg>
    <div>Lorem Ipsum</div>
  </div>
  <div class="why-card" style="left:628px;top:322px">
    <svg width="50" height="58" viewBox="0 0 50 58" fill="none" stroke="currentColor" stroke-width="2.4"><path d="M25 3 5 11v16c0 14 9 23 20 28 11-5 20-14 20-28V11z"/><path d="M15 29l7 7 14-14"/></svg>
    <div>Lorem Ipsum</div>
  </div>
  <div class="why-card" style="left:839px;top:283px">
    <svg width="58" height="60" viewBox="0 0 58 60" fill="none" stroke="currentColor" stroke-width="2"><rect x="12" y="4" width="42" height="20" rx="2"/><path d="M20 11l2 4 3-4M33 11l2 4 3-4M46 11l2 4 3-4"/><path d="M4 34h8v22H4zM12 36l10-12c2-2 5 0 4 3l-2 7h14c3 0 4 3 3 5l-4 14c-1 2-2 3-4 3H12"/></svg>
    <div>Lorem&nbsp; Sit<br>Ipsum</div>
  </div>
</section>

<section class="terms">
  <div class="abs terms-frame">
    <div class="terms-doc" role="document" aria-label="Terms and conditions document preview">
      <div class="col" style="left:40px;top:14px;font-size:7px;line-height:9px">14 Harlow Lane<br>Kelvin Park, Brisbane QLD<br>T 0400 555 018</div>
      <div class="col" style="left:316px;top:14px;font-size:7px;line-height:9px">SUMMIT CREST ADVISORY PTY LTD<br>ABN 12 345 678 901<br>ACN 345 678 901</div>
      <div class="col" style="left:445px;top:17px;width:120px;font-size:13px;font-weight:600;color:#1f2a44">Summit Crest</div>
      <div class="col" style="left:34px;top:60px;width:250px">
        <p class="cl"><b>1.&nbsp;&nbsp; DEFINITIONS AND INTERPRETATION</b></p>
        <p class="cl" style="padding-left:16px"><b>1.1.&nbsp; Definitions</b><br>In this agreement, unless the context otherwise requires:</p>
        <p class="cl" style="padding-left:16px"><b>Accepted Day Rate</b> means, in respect of each supply of an Employee by the Company to the Client, the daily or hourly rate specified in item 3 of the Purchase Order, or if not specified then as published by the Company in its statement of rates as issued from time to time.</p>
        <p class="cl" style="padding-left:16px"><b>Accepted Disbursements</b> means, in respect of each supply of an Employee to the Client, the disbursements specified at item 3 of the Purchase Order.</p>
        <p class="cl" style="padding-left:16px"><b>Agreement</b> means these Standard Terms &amp; Conditions together with the accompanying Purchase Order for the supply of Employees for Professional Services.</p>
        <p class="cl" style="padding-left:16px"><b>Business Day</b> means a day other than a Saturday, Sunday, or public holiday in the State.</p>
        <p class="cl" style="padding-left:16px"><b>Claim</b> means any claim, complaint, demand, proceeding, suit, litigation, action, cause of action or</p>
      </div>
      <div class="col" style="left:300px;top:60px;width:250px">
        <p class="cl" style="padding-left:16px"><b>Employee</b> is employed by the Client.</p>
        <p class="cl" style="padding-left:16px"><b>Purchase Order</b> means the Purchase Order for the supply of Employees for Professional Services accompanying these Standard Terms &amp; Conditions.</p>
        <p class="cl" style="padding-left:16px"><b>Standard Terms &amp; Conditions</b> means the Professional Services Standard Terms &amp; Conditions.</p>
        <p class="cl"><b>INTERPRETATION</b></p>
        <p class="cl" style="padding-left:16px"><b>2.1.</b></p>
        <p class="cl" style="padding-left:16px"><b>2.2.&nbsp; In this agreement:</b></p>
        <p class="cl" style="padding-left:40px">(a)&nbsp; headings are for convenience only and shall not be used in the interpretation or construction of this agreement; and</p>
        <p class="cl" style="padding-left:40px">(b)&nbsp; unless the context otherwise requires:</p>
        <p class="cl" style="padding-left:70px">(i)&nbsp; words importing the singular include the plural and vice versa;</p>
        <p class="cl" style="padding-left:70px">(ii)&nbsp; words importing any gender include the other genders;</p>
        <p class="cl" style="padding-left:70px">(iii)&nbsp; including and similar expressions are not words of limitation;</p>
      </div>
      <div class="doc-bar">Page <span class="pg">1</span> / 10 <span>—</span>
        <svg width="11" height="11" viewBox="0 0 11 11" fill="none" stroke="#eee" stroke-width="1.4"><circle cx="4.5" cy="4.5" r="3.5"/><path d="M7 7l3 3"/></svg>
        <span>+</span></div>
    </div>
  </div>
  <h2 class="terms-title">Terms And Conditions</h2>
  <p class="terms-copy">Lorem ipsum dolor sit amet, consectetur adipiscing elit. In in orci sem. In mattis fermentum pharetra. Sed maximus risus dignissim purus pharetra ac.</p>
</section>

<section class="contact">
  <h2 class="section-title" style="top:3045px">Contact Us</h2>
  <p class="abs contact-intro">Lorem ipsum dolor sit amet, consectetur adipiscing elit. In in orci sem. In mattis fermentum pharetra. Sed vestibulum maximus risus, et dignissim purus pharetra ac.</p>
  <div class="field" style="top:3178px;height:52px">
    <svg width="16" height="18" viewBox="0 0 16 18" fill="none" stroke="#444" stroke-width="1.4"><circle cx="8" cy="5" r="4"/><path d="M1 17c0-4 3-6 7-6s7 2 7 6z"/></svg>Name<i>*</i></div>
  <div class="field" style="top:3244px;height:51px">
    <svg width="18" height="14" viewBox="0 0 18 14" fill="none" stroke="#444" stroke-width="1.4"><rect x="1" y="1" width="16" height="12" rx="1"/><path d="M1 2l8 6 8-6"/></svg>Email<i>*</i></div>
  <div class="field" style="top:3308px;height:51px">
    <svg width="16" height="16" viewBox="0 0 16 16" fill="none" stroke="#444" stroke-width="1.4"><path d="M4 1l2.5 4-2 1.5c1 2.5 3 4.5 5 5.5l1.5-2 4 2.5-1.5 2.5C9 15 1 7 1.5 2.5z"/></svg>Phone</div>
  <div class="field" style="top:3373px;height:103px">
    <svg width="18" height="16" viewBox="0 0 18 16" fill="none" stroke="#444" stroke-width="1.4"><path d="M9 1c4.4 0 8 2.7 8 6s-3.6 6-8 6c-1 0-2-.1-3-.4L2 15l1-3.5C1.8 10.4 1 8.8 1 7c0-3.3 3.6-6 8-6z"/></svg>Message</div>
  <div class="submit"><span class="ring"><svg width="14" height="12" viewBox="0 0 14 12" fill="none" stroke="var(--blue-deep)" stroke-width="1.6"><path d="M1 6h11M8 2l4 4-4 4"/></svg></span>SUBMIT</div>
  <div class="abs map-frame"><div class="map-fill" role="img" aria-label="Street map of Brisbane's northern suburbs showing the office location"></div></div>
</section>

<footer class="abs site-footer">
  <div class="brand"><span class="dot"></span>Summit Crest Advisory</div>
  <nav>
    <a style="left:463px">Home</a>
    <a style="left:574px">About Us</a>
    <a style="left:706px">Services</a>
    <a style="left:831px">Industries</a>
    <a style="left:966px">Contact Us</a>
  </nav>
  <div class="rule" style="top:81px"></div>
  <div class="info" style="left:161px">
    <span class="ic"><svg width="16" height="16" viewBox="0 0 16 16" fill="none" stroke="#fff" stroke-width="1.3"><circle cx="8" cy="8" r="7"/><path d="M1 8h14M8 1c2.5 2.5 2.5 11.5 0 14M8 1c-2.5 2.5-2.5 11.5 0 14"/></svg></span>
    <div>123 Building Name, Street Name,<br>City Name, State XY-123456</div>
  </div>
  <div class="info" style="left:527px">
    <span class="ic"><svg width="15" height="15" viewBox="0 0 16 16" fill="none" stroke="#fff" stroke-width="1.3"><path d="M4 1l2.5 4-2 1.5c1 2.5 3 4.5 5 5.5l1.5-2 4 2.5-1.5 2.5C9 15 1 7 1.5 2.5z"/></svg></span>
    <div><strong>Phone</strong><br>123 456 7890</div>
  </div>
  <div class="info" style="left:791px">
    <span class="ic"><svg width="16" height="13" viewBox="0 0 18 14" fill="none" stroke="#fff" stroke-width="1.3"><rect x="1" y="1" width="16" height="12" rx="1"/><path d="M1 2l8 6 8-6"/></svg></span>
    <div><strong>Email</strong><br>info@scadvisoryhub.com</div>
  </div>
  <div class="rule" style="top:178px"></div>
  <p class="copy">© 2023 &nbsp;<strong>Summit Crest Advisory</strong>. All Rights Reserved.</p>
  <div class="social">WorkCircle<span class="dot"></span></div>
</footer>

</body>
</html>
```